I need cover art for my first album

I am releasing my first album and I need cover art for the CD  packaging. The art would also be used in Tunevale and other streaming services. The music is dark, experimental electronic music. It includes lots of soundscapes with industrial, metallic sounds. Similar artists include Grevhald and Ivor Pennick. The album's concept is inspired by the loneliness and inherent dangers of long-term space travel and living alone in cold, distant space stations.
You can hear a rough cut of one of the tracks for the album at https://echoloft.net/kelvorant/tidegrove.

Colors
Designer to choose colors to be used in the design.
Requirements
Must have
- The design should be abstract and minimalist but not only grayscale. I would like to see color used in ways that convey feelings. Provide a sense of movement.
Should not have
- No images of moons or planets. Please don't be literal with the "space" theme.

```html
<!DOCTYPE html>
<html lang="en">
<head>
<meta charset="utf-8">
<title>Kelvorant – Adrift Beyond The Hull</title>
<link rel="stylesheet" href="https://fonts.googleapis.com/css2?family=Oswald:wght@300;500&display=swap">
<style>
  :root {
    --cobalt: #1e4ea1;
    --magenta: #f0469f;
    --hot-pink: #ee1e8c;
    --violet: #8a2aa6;
    --ember: #f46a1c;
    --sun: #fbd21e;
    --white: #f5f4fa;
  }
  html, body {
    margin: 0;
    padding: 0;
    overflow: hidden;
    background: var(--cobalt);
  }
  .cover {
    position: relative;
    width: 1200px;
    height: 1200px;
    overflow: hidden;
    background: var(--cobalt);
  }
  .cover__artwork {
    position: absolute;
    inset: 0;
    width: 1200px;
    height: 1200px;
  }
  .cover__titles {
    position: absolute;
    top: 57px;
    left: 0;
    width: 1200px;
    text-align: center;
    transform: scaleX(0.84);
    transform-origin: 600px 0;
  }
  .cover__artist {
    margin: 0;
    font-family: "Oswald", "Arial Narrow", sans-serif;
    font-weight: 300;
    font-size: 95px;
    line-height: 1;
    letter-spacing: 3px;
    color: var(--magenta);
  }
  .cover__album {
    margin: 12px 0 0;
    font-family: "Oswald", "Arial Narrow", sans-serif;
    font-weight: 500;
    font-size: 46px;
    line-height: 1;
    letter-spacing: 0;
    color: var(--white);
  }
</style>
</head>
<body>
  <main class="cover">
    <svg class="cover__artwork" viewBox="0 0 1200 1200" role="img" aria-label="Thermal-toned photographic artwork of a bowed winged statue in magenta, violet, orange and yellow, with a city skyline fading into its lower half">
      <defs>
        <radialGradient id="thermal-glow" cx="0.45" cy="0.72" r="0.62">
          <stop offset="0" stop-color="var(--ember)"/>
          <stop offset="0.3" stop-color="var(--hot-pink)"/>
          <stop offset="0.65" stop-color="var(--violet)" stop-opacity="0.85"/>
          <stop offset="1" stop-color="var(--cobalt)" stop-opacity="0"/>
        </radialGradient>
      </defs>
      <rect class="artwork-area" x="0" y="220" width="1200" height="980" fill="url(#thermal-glow)"/>
    </svg>
    <header class="cover__titles">
      <h1 class="cover__artist">KELVORANT</h1>
      <h2 class="cover__album">ADRIFT BEYOND THE HULL</h2>
    </header>
  </main>
</body>
</html>
```